Business Card Design Project - bel soravin group

dear Sirs

we need business card design for our group ( BEL Soravin Group ) , i have got the Logo design of our group from pixel harbor in previous , so all need details relating to our group i think available with you, as well as the the chosen logo design

we hope to provide us with business card logo that to be appropaite and satisfactory to us .

thanks

note : logo design of our group is attached .
Updates

Reason: please extend the deadline of my project for additional 15 days because i didn't received appropriate design for our gruop yet . kindly beaware that i have received 77 design till now , supossed to send me 200-250 design at least . thanks

Target Market(s)

contents
-

name : Korvan EL Mistrani

position : Operation Manager

Industry/Entity Type

Business

Requirements
Must have

• person name

group logo
Nice to have
• logo color matching with back background

```html
<!DOCTYPE html>
<html lang="en">
<head>
<meta charset="utf-8">
<title>BEL Soravin Group – Business Card</title>
<link rel="stylesheet" href="https://fonts.googleapis.com/css2?family=Tinos&display=swap">
<style>
  :root {
    --backdrop: #c8c8c8;
    --card-light: #ffffff;
    --card-dark: #212121;
    --brand-blue: #0b4f91;
    --ink-blue: #124a86;
    --rule-blue: #0d4d8f;
  }
  * { box-sizing: border-box; margin: 0; padding: 0; }
  html, body {
    width: 1029px;
    height: 1200px;
    overflow: hidden;
    background: var(--backdrop);
    font-family: "Tinos", "Times New Roman", serif;
  }
  .card {
    position: absolute;
    width: 895px;
    height: 510px;
    border-radius: 48px;
  }
  .card--front { left: 65px; top: 46px; background: var(--card-light); }
  .card--back  { left: 62px; top: 609px; background: var(--card-dark); }

  .brand {
    position: absolute;
    display: flex;
    align-items: center;
    gap: 22px;
    color: var(--brand-blue);
    font-size: 66px;
    line-height: 1;
    white-space: nowrap;
  }
  .brand__mark {
    width: 44px;
    height: 44px;
    background: var(--brand-blue);
    flex: none;
  }
  .card--front .brand { left: 90px; top: 68px; }
  .card--back .brand  { left: 90px; top: 215px; }

  .person {
    position: absolute;
    left: 10px;
    top: 226px;
    width: 430px;
    text-align: center;
    color: var(--ink-blue);
  }
  .person__name { font-size: 44px; line-height: 1.1; }
  .person__role { font-size: 34px; line-height: 1.2; margin-top: 4px; }

  .divider {
    position: absolute;
    left: 446px;
    top: 204px;
    width: 5px;
    height: 265px;
    background: var(--rule-blue);
  }

  .contact {
    position: absolute;
    left: 491px;
    top: 252px;
    list-style: none;
    color: var(--ink-blue);
    font-size: 26px;
    line-height: 25px;
  }
</style>
</head>
<body>
  <section class="card card--front" aria-label="Card front">
    <div class="brand">
      <span class="brand__mark"></span>
      <span class="brand__name">BEL Soravin Group</span>
    </div>

    <div class="person">
      <p class="person__name">Korvan EL Mistrani</p>
      <p class="person__role">Operation Manager</p>
    </div>

    <div class="divider"></div>

    <ul class="contact">
      <li>tel:</li>
      <li>fax:</li>
      <li>mobile:</li>
      <li>email address:</li>
      <li>website:</li>
      <li>PO. Box:</li>
    </ul>
  </section>

  <section class="card card--back" aria-label="Card back">
    <div class="brand">
      <span class="brand__mark"></span>
      <span class="brand__name">BEL Soravin Group</span>
    </div>
  </section>
</body>
</html>
```